KRT Design Business Card

I need to develop a business card for my real estate design and investment company. Something clean, classic and professional with a modern vibe.

Industry/Entity Type

Real Estate

Font styles to use
Serif
Sans Serif

```html
<!DOCTYPE html>
<html lang="en">
<head>
<meta charset="utf-8">
<title>KRT Design Business Card</title>
<link rel="stylesheet" href="https://fonts.googleapis.com/css2?family=Josefin+Sans:wght@300;400&family=Arimo:wght@400;700&display=swap">
<style>
  :root {
    --page: #e8e8e8;
    --paper: #f4f4f3;
    --ink: #1f1f1f;
    --ink-deep: #151515;
    --ink-soft: #2c2c2c;
    --on-dark: #ffffff;
    --muted-on-dark: #dcdcdc;
  }
  html, body {
    margin: 0;
    width: 1200px;
    height: 720px;
    overflow: hidden;
    background: var(--page);
  }
  .canvas {
    position: relative;
    width: 1200px;
    height: 720px;
  }
  .card {
    position: absolute;
    top: 242px;
    width: 420px;
    height: 240px;
    overflow: hidden;
  }
  .card--front { left: 147px; background: var(--paper); }
  .card--back {
    left: 633px;
    background: linear-gradient(160deg, var(--ink-soft) 0%, var(--ink) 55%, var(--ink-deep) 100%);
  }
  .card__shape {
    position: absolute;
    inset: 0;
    width: 100%;
    height: 100%;
  }
  .brand {
    position: absolute;
    font-family: "Josefin Sans", sans-serif;
    font-weight: 300;
    white-space: nowrap;
  }
  .brand__name {
    display: block;
    font-size: 34px;
    letter-spacing: 2px;
    line-height: 1;
  }
  .brand__tagline {
    display: block;
    font-size: 12.5px;
    margin-top: 10px;
    font-weight: 400;
  }
  .card--front .brand { left: 22px; top: 92px; color: var(--ink); }
  .card--back .brand {
    left: 0; right: 0; top: 86px;
    text-align: center;
    color: var(--on-dark);
  }
  .card--back .brand__name { font-size: 40px; }
  .card--back .brand__tagline { font-size: 13.5px; margin-top: 14px; }
  .details {
    position: absolute;
    right: 26px;
    top: 52px;
    text-align: right;
    font-family: "Arimo", sans-serif;
    color: var(--on-dark);
  }
  .details__name { font-size: 13px; font-weight: 700; margin: 0; }
  .details__role { font-size: 9.5px; margin: 2px 0 0; color: var(--muted-on-dark); }
  .details__address { font-size: 9.5px; line-height: 12.5px; margin: 18px 0 0; color: var(--muted-on-dark); }
  .contact { list-style: none; margin: 22px 0 0; padding: 0; }
  .contact__item {
    display: flex;
    justify-content: flex-end;
    align-items: center;
    gap: 7px;
    font-size: 10px;
    line-height: 12px;
  }
  .contact__icon { width: 10px; height: 9px; flex: none; }
</style>
</head>
<body>
<main class="canvas">

  <section class="card card--front" aria-label="Business card front">
    <svg class="card__shape" viewBox="0 0 525 299" preserveAspectRatio="none" aria-hidden="true">
      <polygon points="349,0 525,0 525,299 208,299" fill="var(--ink)"/>
      <polygon points="331,0 341,0 242,272" fill="var(--ink)"/>
    </svg>

    <div class="brand">
      <span class="brand__name">KRT Design</span>
      <span class="brand__tagline">Design and Productions</span>
    </div>

    <div class="details">
      <p class="details__name">Daniel Reyes</p>
      <p class="details__role">Founder &amp; CEO</p>
      <p class="details__address">Here your compnay or home<br>address</p>
      <ul class="contact">
        <li class="contact__item">+975 214 368
          <svg class="contact__icon" viewBox="0 0 10 9" aria-hidden="true"><path d="M1 3 Q5 0 9 3 L8 4 L6.5 3 L3.5 3 L2 4 Z M3 4 H7 L8.5 8.5 H1.5 Z" fill="var(--on-dark)"/></svg>
        </li>
        <li class="contact__item">+975 632 107
          <svg class="contact__icon" viewBox="0 0 10 9" aria-hidden="true"><rect x="3" y="0.5" width="4.5" height="8" rx="0.8" fill="none" stroke="var(--on-dark)" stroke-width="1"/></svg>
        </li>
        <li class="contact__item">info@krtdesign.com
          <svg class="contact__icon" viewBox="0 0 10 9" aria-hidden="true"><rect x="0.5" y="1" width="9" height="7" fill="var(--on-dark)"/><path d="M0.5 1 L5 5 L9.5 1 M0.5 8 L4 4.2 M9.5 8 L6 4.2" stroke="var(--ink)" stroke-width="0.8" fill="none"/></svg>
        </li>
        <li class="contact__item">www.krtdesign.com
          <svg class="contact__icon" viewBox="0 0 10 9" aria-hidden="true"><rect x="0.5" y="0.5" width="9" height="6" fill="none" stroke="var(--on-dark)" stroke-width="1"/><rect x="3.5" y="7.5" width="3" height="1" fill="var(--on-dark)"/></svg>
        </li>
      </ul>
    </div>
  </section>

  <section class="card card--back" aria-label="Business card back">
    <div class="brand">
      <span class="brand__name">KRT Design</span>
      <span class="brand__tagline">Design and Productions</span>
    </div>
  </section>

</main>
</body>
</html>
```